Vyrella Motion Design
Would like the design to go over the page in a way that can type over it.
We are a personal training and small group studio
Want it to be professional and classy
Reason: Asked for some modifications on a few designs, want to give the designers time to do this
Target Market(s)
All age groups, sports professionals as well as business professionals, families
Industry/Entity Type
Training
Requirements
Must have
- Must have Vyrella Motion Studio
Mira Pendleby
314 Calloway Street
Marbeck Vale
Norland Territory 6241
Phone: 0497318260
Nice to have
- Professional classy fonts
Colour
Should not have
- Clip art
Balloons

```html
<!DOCTYPE html>
<html lang="en">
<head>
<meta charset="utf-8">
<title>Vyrella Motion Studio — Stationery</title>
<link rel="stylesheet" href="https://fonts.googleapis.com/css2?family=Montserrat:wght@400;500&display=swap">
<style>
  :root {
    --page-bg: #ffffff;
    --paper: #f0ecda;
    --brand-orange: #f26722;
    --brand-slate: #2f3d56;
    --arc-light: #b9d3de;
    --arc-dark: #8a9db8;
    --ink: #2b2b2b;
  }
  html, body {
    margin: 0;
    padding: 0;
    width: 1200px;
    height: 1017px;
    overflow: hidden;
    background: var(--page-bg);
  }
  .stationery {
    display: block;
    width: 1200px;
    height: 1017px;
    font-family: "Montserrat", "Helvetica Neue", sans-serif;
  }
  .paper { fill: var(--paper); }
  .flap { fill: var(--brand-orange); }
  .accent-rule { fill: var(--brand-orange); }
  .arc { fill: url(#arcGradient); }
  .wordmark {
    fill: var(--brand-slate);
    font-weight: 500;
    letter-spacing: 0.5px;
  }
  .return-address {
    fill: var(--ink);
    font-size: 7px;
    font-weight: 400;
  }
</style>
</head>
<body>
<svg class="stationery" viewBox="0 0 1200 1017" xmlns="http://www.w3.org/2000/svg">
  <defs>
    <linearGradient id="arcGradient" x1="0" y1="0" x2="1" y2="1">
      <stop offset="0" style="stop-color:#b9d3de"/>
      <stop offset="1" style="stop-color:#8a9db8"/>
    </linearGradient>
  </defs>

  <g class="envelope-back">
    <path class="flap" d="M78,368 Q78,362 86,363 C140,368 180,356 220,340 C280,318 360,318 420,329 Q437,333 437,345 L437,381 L78,381 Z"/>
    <rect class="paper" x="78" y="380" width="359" height="178"/>
    <path class="arc" d="M207,399 Q100,430 78,556 L81,556 Q110,440 207,399 Z"/>
    <path class="arc" d="M306,399 Q415,430 437,556 L434,556 Q405,440 306,399 Z"/>
    <text class="wordmark" x="257" y="458" font-size="12" text-anchor="middle">Vyrella Motion Studio</text>
  </g>

  <g class="envelope-front">
    <path class="flap" d="M67,590 Q72,566 150,563 C230,561 262,575 300,592 C340,609 380,611 418,605 Q426,604 426,612 L426,621 L67,621 Z"/>
    <rect class="paper" x="67" y="620" width="359" height="180"/>
    <text class="return-address" x="82" y="794" textLength="311" lengthAdjust="spacingAndGlyphs">Mira Pendleby, 314 Calloway Street, Marbeck Vale, Norland Territory 6241. Phone# 0497318260</text>
  </g>

  <g class="letterhead">
    <rect class="paper" x="498" y="83" width="596" height="843" rx="26" ry="26"/>
    <text class="wordmark" x="795" y="152" font-size="22" text-anchor="middle">Vyrella Motion Studio</text>
    <path class="arc" d="M710,253 Q525,300 496,512 L501,512 Q535,315 710,253 Z"/>
    <path class="arc" d="M876,253 Q1062,300 1092,512 L1086,512 Q1050,315 876,253 Z"/>
    <path class="accent-rule" d="M555,902 L1031,902 Q1000,907 980,907 L605,907 Q585,907 555,902 Z"/>
  </g>
</svg>
</body>
</html>
```